Day of the Lord Infographic

I would like an infographic, which will be placed on a website. If different sections could be clickable that would be great. I have included a picture file to understand the basic flow and layout Since this will be on a website the image can be longer than a standard 8x11, in fact, that is preferred.
The graphic should be in about the same layout just much nicer. This is indicating that these events will all occur on what is the Day of the Lord in the order that they are laid out in the picture. I don't necessarily need lines except the 5 dotted or dashed lines (might have to enlarge picture)
Maybe the Day of the Lord is a title or on the side.
Next I have included an RTF file that has the information of the notes for each section. These are scripture verses that need to somehow be incorporated. If a clickable option is available then I can set these up on the website, if not then these need to somehow need to be incorporated.
This project is for the education ministry on www.lanternbrookhall.org. Colors can be complementary or coordinating.

```html
<!DOCTYPE html>
<html lang="en">
<head>
<meta charset="utf-8">
<title>Day of the Lord</title>
<link href="https://fonts.googleapis.com/css2?family=Roboto:wght@400;500;700;900&display=swap" rel="stylesheet">
<style>
  :root{
    --teal-dark:#07607e;
    --teal-line:#0b5f78;
    --teal-ref:#0e6a86;
    --tan:#c9a27a;
    --purple:#7b5a8d;
    --sea:#6ea3a8;
    --ink:#1d1d1d;
    --white:#ffffff;
    --node-fill:#e8edf0;
  }
  html,body{margin:0;padding:0;width:1200px;height:927px;overflow:hidden}
  body{font-family:"Roboto",Arial,sans-serif}
  .canvas{
    position:relative;width:1200px;height:927px;overflow:hidden;
    background:
      radial-gradient(ellipse 55% 60% at 0% 0%, #6aaef5 0%, rgba(106,174,245,0) 70%),
      radial-gradient(ellipse 50% 60% at 100% 10%, #ffae8a 0%, rgba(255,174,138,0) 75%),
      radial-gradient(ellipse 55% 55% at 100% 100%, #ffaaa0 0%, rgba(255,170,160,0) 75%),
      radial-gradient(ellipse 45% 50% at 0% 55%, #bfe3ea 0%, rgba(191,227,234,0) 80%),
      linear-gradient(160deg,#b7d0ee 0%,#f5eac8 45%,#fbe6c4 65%,#ffc3a8 100%);
  }
  .diagram{position:absolute;left:0;top:0;width:1200px;height:927px}
  .connector{fill:none;stroke:var(--teal-line);stroke-width:3}
  .connector--dashed{stroke-dasharray:10 8}
  .node{fill:var(--node-fill);stroke:var(--teal-line);stroke-width:3}
  .node--outlined{fill:var(--node-fill);stroke:var(--purple);stroke-width:3}
  .frame{fill:none;stroke:var(--teal-line);stroke-width:3}
  .frame--thin{fill:none;stroke:var(--teal-line);stroke-width:2}
  .pill-white{fill:var(--white)}
  .pill-tan{fill:var(--tan)}
  .pill-teal{fill:var(--teal-dark)}
  .pill-purple{fill:var(--purple)}
  .pill-sea{fill:var(--sea)}
  .badge-tan{fill:var(--tan)}
  .badge-purple{fill:var(--purple)}
  .badge-sea{fill:var(--sea)}
  .icon-line{fill:none;stroke:var(--white);stroke-width:5;stroke-linecap:round;stroke-linejoin:round}
  .title{font-weight:900;font-size:84px;letter-spacing:7px;fill:var(--white)}
  .title-refs{font-size:22px;fill:var(--white)}
  .head{font-weight:500;font-size:31px;fill:var(--ink)}
  .head-lg{font-weight:400;font-size:34px;fill:var(--ink)}
  .ref{font-size:22px;fill:var(--teal-ref)}
  .ref-dark{font-size:22px;fill:var(--ink)}
  .seven{font-weight:700;font-size:52px;fill:var(--white)}
  .rule{stroke:var(--teal-line);stroke-width:2}
  .rule-light{stroke:#8a9aa3;stroke-width:1.5}
</style>
</head>
<body>
<main class="canvas">
<svg class="diagram" viewBox="0 0 2184 1688" xmlns="http://www.w3.org/2000/svg">
  <defs>
    <clipPath id="heroClip"><circle cx="1092" cy="655" r="226"/></clipPath>
    <linearGradient id="heroTone" x1="0" y1="0" x2="1" y2="1">
      <stop offset="0" stop-color="#3b2a6e"/>
      <stop offset=".35" stop-color="#e08a3a"/>
      <stop offset=".6" stop-color="#f4c27a"/>
      <stop offset="1" stop-color="#3f8fe0"/>
    </linearGradient>
  </defs>

  <g class="connectors">
    <line class="connector" x1="601" y1="366" x2="852" y2="515"/>
    <line class="connector" x1="1585" y1="369" x2="1353" y2="505"/>
    <line class="connector" x1="1353" y1="806" x2="1579" y2="924"/>
    <line class="connector" x1="1288" y1="887" x2="1545" y2="1120"/>
    <line class="connector" x1="1092" y1="958" x2="1092" y2="1013"/>
    <path class="connector" d="M1826 415 V457 H1717 V492"/>
    <path class="connector" d="M1876 415 V457 H1985 V492"/>
    <line class="connector" x1="1788" y1="1247" x2="1788" y2="1312"/>
    <path class="connector" d="M1519 1176 H1480 V1438 H1404"/>
    <path class="connector" d="M1065 1160 V1200 H956 V1240"/>
    <path class="connector" d="M1115 1160 V1200 H1268 V1245"/>
    <path class="connector" d="M948 1532 V1585 H1197"/>
    <path class="connector" d="M130 705 H60 V1612 H1205"/>
    <line class="connector" x1="194" y1="412" x2="194" y2="1100"/>
    <line class="connector connector--dashed" x1="194" y1="1110" x2="194" y2="1392"/>
    <path class="connector" d="M697 950 V1140 H459 V1200"/>
    <path class="connector" d="M529 1258 H745 V1076 H815"/>
    <line class="connector" x1="254" y1="1455" x2="298" y2="1455"/>
  </g>

  <g class="title-block">
    <rect x="612" y="55" width="960" height="207" rx="103" class="pill-teal"/>
    <text x="1093" y="140" text-anchor="middle" class="title">DAY OF THE LORD</text>
    <line x1="695" y1="157" x2="1490" y2="157" stroke="#5e9fb3" stroke-width="2"/>
    <text x="1093" y="189" text-anchor="middle" class="title-refs">1 Thess 4:13-5:9, 2 Thess 2:1-12, Isa 13:6,9; Is 34:8; Jer 46:10; Ezek 13:5,</text>
    <text x="1093" y="215" text-anchor="middle" class="title-refs">30:3; Joel 1:15, 2:1,2:11,2:31,3:14; Amos 5:18,20 Obad 15; Zeph 1:7,14; Mal</text>
    <text x="1093" y="241" text-anchor="middle" class="title-refs">4:5; Acts 2:20,1 Cor 5:5;1 Thess 5:2; 2 Thess 2:2; 2 Pet 3:10 Isa 2-5; Zech 14</text>
  </g>

  <g class="hub">
    <circle cx="1092" cy="655" r="302" class="frame"/>
    <circle cx="1092" cy="655" r="280" class="pill-teal"/>
    <circle cx="1092" cy="655" r="241" fill="none" stroke="#ffffff" stroke-width="3"/>
    <g clip-path="url(#heroClip)">
      <rect x="860" y="425" width="465" height="470" fill="url(#heroTone)" role="img" aria-label="Illustration of a radiant figure in bright heavenly light"/>
      <rect x="860" y="672" width="465" height="230" fill="#ffffff" opacity=".82"/>
    </g>
    <text x="1101" y="708" text-anchor="middle" class="head">Day of clouds, Darkness</text>
    <text x="1101" y="742" text-anchor="middle" class="head">Signs Heavens</text>
    <line x1="940" y1="758" x2="1262" y2="758" class="rule-light"/>
    <text x="1092" y="786" text-anchor="middle" class="ref-dark">Zeph 1:7-15, Isa 13:1-16,Eze</text>
    <text x="1092" y="812" text-anchor="middle" class="ref-dark">30:1-9,Amos 5:18,20, Joel</text>
    <text x="1092" y="838" text-anchor="middle" class="ref-dark">2:2,Amos 8:3,9,13,</text>
    <text x="1092" y="865" text-anchor="middle" class="ref-dark">Mat 24:29</text>
  </g>

  <g class="event event--second-coming">
    <rect x="60" y="267" width="545" height="145" rx="72" class="frame"/>
    <rect x="77" y="280" width="513" height="118" rx="59" class="pill-tan"/>
    <rect x="95" y="292" width="480" height="94" rx="47" class="pill-white"/>
    <text x="335" y="332" text-anchor="middle" class="head">Second Coming the Lord</text>
    <text x="335" y="364" text-anchor="middle" class="ref">1 thess 4:13-5:9, 2 Thess 2:1-12</text>
  </g>

  <g class="event event--judgment">
    <rect x="1578" y="270" width="547" height="145" rx="72" class="frame"/>
    <rect x="1597" y="283" width="513" height="120" rx="60" class="pill-tan"/>
    <rect x="1614" y="295" width="480" height="95" rx="47" class="pill-white"/>
    <text x="1852" y="326" text-anchor="middle" class="head">Judgment</text>
    <text x="1852" y="355" text-anchor="middle" class="ref">Mal 4:5, Isa 13:1-16,Eze</text>
    <text x="1852" y="381" text-anchor="middle" class="ref">30:1-9,Obd 15, Isa 4:4,2 Pet 3:10</text>
  </g>

  <g class="event event--nations">
    <path d="M1647 558 A70 70 0 0 0 1787 558" class="frame"/>
    <circle cx="1717" cy="558" r="60" class="badge-tan"/>
    <g class="icon-line">
      <circle cx="1717" cy="552" r="30"/>
      <ellipse cx="1717" cy="552" rx="13" ry="30"/>
      <line x1="1687" y1="552" x2="1747" y2="552"/>
      <line x1="1691" y1="537" x2="1743" y2="537"/>
      <line x1="1691" y1="567" x2="1743" y2="567"/>
    </g>
    <text x="1717" y="672" text-anchor="middle" class="head">Nations</text>
    <line x1="1645" y1="682" x2="1790" y2="682" class="rule"/>
    <text x="1714" y="709" text-anchor="middle" class="ref">Eze 30:1-9, Obd,Zeph</text>
    <text x="1714" y="734" text-anchor="middle" class="ref">1, Isa 34:1-9,Zech 14</text>
  </g>
  <g class="event event--valley">
    <path d="M1915 558 A70 70 0 0 0 2055 558" class="frame"/>
    <circle cx="1985" cy="558" r="60" class="badge-tan" role="img" aria-label="Crown icon"/>
    <text x="1985" y="673" text-anchor="middle" class="head">Valley of</text>
    <text x="1985" y="709" text-anchor="middle" class="head">Jehoshaphat</text>
    <line x1="1883" y1="720" x2="2088" y2="720" class="rule"/>
    <text x="1983" y="750" text-anchor="middle" class="ref">Joel 3:12</text>
  </g>

  <g class="event event--battle">
    <rect x="1578" y="866" width="547" height="144" rx="72" class="frame"/>
    <rect x="1597" y="878" width="513" height="120" rx="60" class="pill-teal"/>
    <rect x="1614" y="890" width="480" height="95" rx="47" class="pill-white"/>
    <text x="1850" y="921" text-anchor="middle" class="head">Day of Battle</text>
    <text x="1852" y="949" text-anchor="middle" class="ref">Mal 4(5), Isa 13:1-16,Joel</text>
    <text x="1852" y="975" text-anchor="middle" class="ref">2:2-11,Zech 14:3,5,Isa 13:4</text>
  </g>

  <g class="event event--wrath">
    <rect x="1520" y="1105" width="545" height="143" rx="71" class="frame"/>
    <rect x="1537" y="1117" width="513" height="118" rx="59" class="pill-sea"/>
    <rect x="1555" y="1130" width="477" height="92" rx="46" class="pill-white"/>
    <text x="1790" y="1166" text-anchor="middle" class="head">Wrath of God</text>
    <text x="1788" y="1201" text-anchor="middle" class="ref">Zeph 1:7-15,Isa 13:1-16,Joel 1:15,Isa 34:1-9</text>
  </g>
  <g class="event event--bowls">
    <path d="M1718 1372 A70 70 0 0 0 1858 1372" class="frame"/>
    <circle cx="1788" cy="1372" r="60" class="badge-sea"/>
    <circle cx="1788" cy="1372" r="36" fill="none" stroke="#ffffff" stroke-width="5"/>
    <text x="1788" y="1390" text-anchor="middle" class="seven">7</text>
    <text x="1788" y="1483" text-anchor="middle" class="head">7 Bowls of Wrath</text>
  </g>

  <g class="event event--rapture">
    <rect x="817" y="1015" width="543" height="145" rx="72" class="frame"/>
    <rect x="834" y="1028" width="511" height="117" rx="58" class="pill-purple"/>
    <rect x="851" y="1040" width="479" height="93" rx="46" class="pill-white"/>
    <text x="1092" y="1080" text-anchor="middle" class="head">Rapture of elect</text>
    <text x="1092" y="1117" text-anchor="middle" class="ref">1 Thess 4:13-17</text>
  </g>

  <g class="event event--resurrection">
    <path d="M886 1300 A70 70 0 0 0 1026 1300" class="frame"/>
    <circle cx="956" cy="1300" r="60" class="badge-purple"/>
    <g class="icon-line">
      <rect x="920" y="1272" width="24" height="24" transform="rotate(-30 932 1284)"/>
      <circle cx="987" cy="1284" r="12"/>
      <path d="M944 1340 L956 1318 L968 1340 Z"/>
      <path d="M950 1272 Q965 1264 976 1274"/>
      <path d="M990 1308 Q984 1324 970 1330"/>
      <path d="M924 1305 Q928 1322 940 1330"/>
    </g>
    <rect x="785" y="1388" width="336" height="144" rx="8" class="frame--thin"/>
    <text x="955" y="1422" text-anchor="middle" class="head-lg">Resurrection dead,</text>
    <text x="955" y="1453" text-anchor="middle" class="head-lg">transformation living</text>
    <text x="955" y="1484" text-anchor="middle" class="head-lg">into new body</text>
    <text x="950" y="1511" text-anchor="middle" class="ref">1 Cor 15 (23,51-52)</text>
  </g>

  <g class="event event--protects">
    <path d="M1198 1305 A70 70 0 0 0 1338 1305" class="frame"/>
    <circle cx="1268" cy="1305" r="60" class="badge-purple" role="img" aria-label="Winged guardian icon"/>
    <rect x="1160" y="1388" width="244" height="127" rx="8" class="frame--thin"/>
    <text x="1279" y="1424" text-anchor="middle" class="head">Protects from</text>
    <text x="1279" y="1458" text-anchor="middle" class="head">wrath of God</text>
    <text x="1281" y="1487" text-anchor="middle" class="ref">1 Thess 4:13-5:9,</text>
    <text x="1281" y="1508" text-anchor="middle" class="ref">Zeph 2:3</text>
  </g>

  <g class="event event--meet">
    <path d="M1198 1585 A70 70 0 0 0 1338 1585" class="frame"/>
    <circle cx="1268" cy="1585" r="60" class="badge-purple" role="img" aria-label="Icon of a figure lifting up a believer"/>
    <text x="1383" y="1572" class="head">Meet the Lord</text>
    <text x="1383" y="1606" class="head">in cloud</text>
    <line x1="1383" y1="1617" x2="1562" y2="1617" class="rule"/>
    <text x="1383" y="1645" class="ref">(1 Thess 4:13-5:9)</text>
  </g>

  <g class="timeline">
    <g class="step">
      <path d="M124 537 A70 70 0 0 0 264 537" class="frame"/>
      <circle cx="194" cy="537" r="60" class="badge-tan" role="img" aria-label="Open heavenly gate icon"/>
      <text x="459" y="548" text-anchor="middle" class="head">Descend From Heaven</text>
      <line x1="308" y1="558" x2="610" y2="558" class="rule"/>
      <text x="459" y="588" text-anchor="middle" class="ref">1 Thess 4:13-5:9</text>
    </g>
    <g class="step">
      <path d="M124 703 A70 70 0 0 0 264 703" class="frame"/>
      <circle cx="194" cy="703" r="60" class="badge-tan"/>
      <path class="icon-line" d="M166 722 Q150 722 152 706 Q154 692 168 694 Q168 674 188 672 Q206 670 212 686 Q232 684 236 702 Q238 722 218 722 Z"/>
      <text x="458" y="717" text-anchor="middle" class="head">Comes in/on the clouds</text>
      <line x1="300" y1="728" x2="618" y2="728" class="rule"/>
      <text x="459" y="758" text-anchor="middle" class="ref">Matthew 24:30-31</text>
    </g>
    <g class="step">
      <path d="M124 866 A70 70 0 0 0 264 866" class="frame"/>
      <circle cx="194" cy="866" r="60" class="badge-tan" role="img" aria-label="Angel icon"/>
      <rect x="284" y="838" width="464" height="112" rx="8" class="frame--thin"/>
      <text x="517" y="873" text-anchor="middle" class="head">Voice of command to Angels to</text>
      <text x="517" y="907" text-anchor="middle" class="head">Gather elect</text>
      <text x="516" y="938" text-anchor="middle" class="ref">1 thess 4:13-5:9, Mat 24:30-31</text>
    </g>
    <g class="step">
      <path d="M124 1042 A70 70 0 0 0 264 1042" class="frame"/>
      <circle cx="194" cy="1042" r="60" class="badge-tan"/>
      <g class="icon-line">
        <path d="M188 1082 V1048 H172 V1034 H188 V1018 H200 V1034 H216 V1048 H200 V1082 Z"/>
        <path d="M160 1012 L166 1018 M228 1012 L222 1018 M194 1000 V1008 M150 1036 H158 M230 1036 H238"/>
      </g>
      <text x="451" y="1055" text-anchor="middle" class="head">Trumpet of God (last)</text>
      <line x1="306" y1="1066" x2="596" y2="1066" class="rule"/>
      <text x="458" y="1095" text-anchor="middle" class="ref">1 Thess 4:13-5:9, Matt 24:30-31,</text>
      <text x="458" y="1121" text-anchor="middle" class="ref">1 Cor 15(52)</text>
    </g>
    <g class="step">
      <path d="M194 1385 A70 70 0 0 0 194 1525" class="frame"/>
      <circle cx="194" cy="1455" r="60" class="badge-tan"/>
      <g class="icon-line">
        <path d="M150 1478 L172 1440 L186 1462 L200 1432 L234 1478"/>
        <line x1="146" y1="1478" x2="236" y2="1478"/>
        <circle cx="216" cy="1434" r="6"/>
      </g>
      <text x="480" y="1463" text-anchor="middle" class="head">Will Stand on Mount</text>
      <text x="480" y="1499" text-anchor="middle" class="head">of Olives</text>
      <line x1="345" y1="1512" x2="615" y2="1512" class="rule"/>
      <text x="480" y="1543" text-anchor="middle" class="ref">Zech 14:2</text>
    </g>
  </g>

  <g class="event event--angels-gather">
    <path d="M389 1262 A70 70 0 0 0 529 1262" class="frame"/>
    <circle cx="459" cy="1260" r="60" class="badge-tan"/>
    <path class="icon-line" d="M459 1290 L432 1262 Q422 1248 434 1238 Q448 1230 459 1244 Q470 1230 484 1238 Q496 1248 486 1262 Z"/>
    <path class="icon-line" d="M428 1248 Q412 1242 404 1250 Q414 1262 428 1258 M490 1248 Q506 1242 514 1250 Q504 1262 490 1258"/>
    <text x="459" y="1366" text-anchor="middle" class="head">Angels gather elect</text>
    <line x1="326" y1="1378" x2="591" y2="1378" class="rule"/>
    <text x="458" y="1405" text-anchor="middle" class="ref">Mat 24:30-31</text>
  </g>

  <g class="nodes">
    <circle cx="601" cy="366" r="10" class="node"/>
    <circle cx="1353" cy="505" r="10" class="node"/>
    <circle cx="1353" cy="806" r="10" class="node"/>
    <circle cx="1288" cy="887" r="10" class="node"/>
    <circle cx="1092" cy="958" r="10" class="node"/>
    <circle cx="1092" cy="1013" r="10" class="node"/>
    <circle cx="1585" cy="369" r="10" class="node"/>
    <circle cx="1717" cy="492" r="10" class="node"/>
    <circle cx="1985" cy="492" r="10" class="node"/>
    <circle cx="1579" cy="924" r="10" class="node" style="fill:var(--teal-dark)"/>
    <circle cx="1545" cy="1120" r="10" class="node"/>
    <circle cx="1519" cy="1176" r="10" class="node"/>
    <circle cx="1788" cy="1247" r="10" class="node"/>
    <circle cx="815" cy="1076" r="10" class="node--outlined"/>
    <circle cx="1065" cy="1160" r="10" class="node--outlined"/>
    <circle cx="1115" cy="1160" r="10" class="node--outlined"/>
    <circle cx="956" cy="1240" r="10" class="node--outlined"/>
    <circle cx="1268" cy="1245" r="10" class="node--outlined"/>
    <circle cx="948" cy="1532" r="10" class="node--outlined"/>
    <circle cx="1404" cy="1438" r="10" class="node--outlined"/>
    <circle cx="1197" cy="1585" r="8" class="node--outlined"/>
    <circle cx="1205" cy="1612" r="8" class="node--outlined"/>
    <circle cx="697" cy="950" r="10" class="node"/>
    <circle cx="459" cy="1200" r="10" class="node"/>
    <circle cx="529" cy="1258" r="8" class="node"/>
    <circle cx="298" cy="1455" r="10" class="node--outlined"/>
  </g>
</svg>
</main>
</body>
</html>
```